Postcard for Dental Lab to Dental Lab

We are a wholesale Outsourcing Dental Lab. We are looking for a postcard design that will attract new customers and accounts. We market to Only other dental Labs. We are looking for a design based around "new year resolutions list for a dental lab" Our logo colors are green, gold and white. We want a box with a check mark in it showing that our lab has meet all of the new year resolution lists.

We are looking for a new years resolutions postcard. It should have a professional look as we are sending it to dental Labs.

Maybe something that shows a fresh start and new year. The main focus point would be a "New years resolution" List. This list should look like it has been written on paper. It should list things like
The heading should read. "New Years Resolutions list"
1. Work less Hours while maintaining current income
2. Expand current dental Lab
3. Make More money with Less headaches.
4. Gain more freedom from long hours behind bench.

Then another heading: "Ways to achieve resolutions list"
"Find outsourcing dental lab that offers..."

1. Find a experienced full service dental Lab

2. Lab that is FDA and KTRC certified.

3. Competitive prices.

4. Has consistent quality restorations and products.

5. BRIVEN WORKS
That was easy.

On the back of the card we would like some bullet points.
1. ISO 9001, 13485 and FDA Certified.
2. Restorative Goods Quality Review Scheme (RGQRS) certified.
3. 5 year warranty on fixed and 2 years on removable.
4. Local Customer service in Phoenix Arizona assigned to your office and cases.
5. Higher productivity- Allows you to provide more units from your lab with the same number of technicians.

Here are two customer quotes that we can use.
"Impressive work....Better than what we can do locally!..."

"Thanks for your wonderful service, our business is increasing by 20% per month..."

Please have and area for the mailing address and return address. We are looking for a headline that is large on the front of the post card that will grab attention. Maybe an image of sparklers or fireworks or something with a new years new start.
Keep the designs coming as we are really needing to get this design finished quick.
Thanks!

I have uploaded a sample of what we are looking for. This is from a diffrent dental lab but with the same idea. Please look at this design but include what we have asked for. thank you
Updates

This flyer will be 6” x 11” with an eye catching basic design on the front and some more detailed info on the back.  I would like to focus on getting a great front design and then we can work on making the back coordinate.  Can have some brighter colors for the “New Year’s Resolution” part (look festive and eye catching) Maybe some Fireworks in the background

This flyer will be an introduction to our business in new areas that we have not worked in before. 
The concept is to introduce our lab, let them know we will be offering our services in their regions and do it in a creative, eye catching way. 

The concept I would like for the flyer is a new year’s resolution list that has a list of things they need to complete their goals.  The list is needs to look like a piece of paper with a visually appealing header of “NEW YEAR’S RESOLUTION” and a hand written look of the rest of what is below. The bullet points need to be boxes and they need check marks in them like they put a check mark in the boxes by hand.

On the front of the postcard there needs to be a place for our phone number 855-314-9087 and then an area to place "Special Trial offer" 5 free PFM'S!

Reason: I would like to provide more feed back. Due to the holiday we will be extending the deadline. Thank you for the designs please keep them coming.

Reason: Still looking for a good design. please keep them coming. Thank you

Target Market(s)

Dental LAB OWNERS.

Industry/Entity Type

Dental

Requirements
Must have
• New Year resolutions theme. Looking for a list that is written on a piece of paper with checkboxes next to every one of the lists.

```html
<!DOCTYPE html>
<html lang="en">
<head>
<meta charset="utf-8">
<title>Briven Works – New Year Postcard</title>
<link href="https://fonts.googleapis.com/css2?family=Architects+Daughter&family=Sniglet:wght@400;800&display=swap" rel="stylesheet">
<style>
  :root {
    --backdrop: #7b3f22;
    --green: #0f5a2c;
    --gold: #d9a400;
    --gold-light: #f4d23c;
    --glow: #fff3a0;
    --ink: #1c1c1c;
    --white: #ffffff;
  }
  * { margin: 0; padding: 0; box-sizing: border-box; }
  html, body { width: 1100px; height: 1200px; overflow: hidden; }
  body { background: var(--backdrop); position: relative; font-family: "Architects Daughter", cursive; }

  .postcard { position: absolute; left: 61px; width: 972px; height: 529px; background: var(--white); overflow: hidden; }
  .postcard--front { top: 43px; }
  .postcard--back { top: 612px; }
  .postcard__art { position: absolute; inset: 0; width: 100%; height: 100%; }

  .brand { position: absolute; left: 27px; top: 18px; display: flex; align-items: center; gap: 8px; }
  .brand__mark { width: 34px; height: 34px; border-radius: 50%; background: var(--green); }
  .brand__name { font-size: 18px; color: var(--green); letter-spacing: 0.5px; white-space: nowrap; }

  .list-heading { position: absolute; font-family: "Sniglet", sans-serif; font-weight: 400; color: var(--green);
    text-transform: uppercase; letter-spacing: 0.5px; white-space: nowrap;
    text-shadow: -1px -1px 0 #fff, 1px -1px 0 #fff, -1px 1px 0 #fff, 1px 1px 0 #fff, 2px 2px 2px rgba(0,0,0,0.35); }
  .list-heading--achieve { left: 139px; top: 157px; font-size: 19px; }
  .list-heading--resolutions { left: 525px; top: 28px; font-size: 22px; }

  .bullet-list { position: absolute; list-style: none; text-transform: uppercase; color: var(--ink); }
  .bullet-list li { position: relative; }
  .bullet-list li::before { content: ""; position: absolute; border-radius: 50%; background: var(--ink); }

  .bullet-list--achieve { left: 117px; top: 192px; width: 380px; font-size: 20px; line-height: 20px; }
  .bullet-list--achieve li { padding-left: 34px; margin-bottom: 17px; }
  .bullet-list--achieve li::before { left: 0; top: 6px; width: 9px; height: 9px; }

  .bullet-list--features { left: 92px; top: 187px; width: 380px; font-size: 16px; line-height: 16px; }
  .bullet-list--features li { padding-left: 19px; margin-bottom: 20px; }
  .bullet-list--features li::before { left: 0; top: 4px; width: 8px; height: 8px; }

  .resolution-list { position: absolute; left: 517px; top: 77px; width: 430px; list-style: none;
    text-transform: uppercase; color: var(--ink); font-size: 17px; line-height: 20px; }
  .resolution-list li { position: relative; padding-left: 38px; margin-bottom: 26px; }
  .resolution-list svg { position: absolute; left: 0; top: -2px; width: 26px; height: 26px; }

  .phone { position: absolute; left: 703px; top: 422px; display: flex; align-items: center; gap: 12px;
    color: var(--white); font-family: "Sniglet", sans-serif; font-size: 30px; letter-spacing: 1px; }
  .phone__icon { width: 30px; height: 30px; border-radius: 5px; background: var(--white); display: flex; align-items: center; justify-content: center; }
  .phone__icon svg { width: 22px; height: 22px; }

  .testimonial { position: absolute; color: var(--white); font-family: "Sniglet", sans-serif; text-transform: uppercase;
    text-align: center; font-size: 17px; line-height: 22px; letter-spacing: 0.5px; }
  .testimonial--front { left: 600px; top: 466px; width: 360px; }
  .testimonial--back { left: 470px; top: 471px; width: 500px; }

  .trial-offer { position: absolute; left: 25px; top: 491px; color: var(--white); font-size: 12px; text-transform: uppercase; }

  .mailing-divider { position: absolute; left: 568px; top: 45px; width: 2px; height: 343px; background: var(--ink); }
  .stamp-box { position: absolute; left: 865px; top: 25px; width: 82px; height: 92px; border: 3px solid var(--ink); }
  .address-line { position: absolute; left: 595px; width: 352px; height: 2px; background: var(--ink); }
</style>
</head>
<body>

<section class="postcard postcard--front">
  <svg class="postcard__art" viewBox="0 0 790 430" preserveAspectRatio="none" aria-hidden="true">
    <defs>
      <radialGradient id="glowFront" cx="0.7" cy="0.5" r="0.8">
        <stop offset="0" stop-color="#fff3a0"/>
        <stop offset="0.6" stop-color="#fbe985"/>
        <stop offset="1" stop-color="#fff8cf"/>
      </radialGradient>
      <linearGradient id="goldBand" x1="0" x2="1">
        <stop offset="0" stop-color="#f4d23c"/>
        <stop offset="0.6" stop-color="#d9a400"/>
        <stop offset="1" stop-color="#7a5a10"/>
      </linearGradient>
    </defs>
    <path d="M0,250 C70,130 200,30 405,0 L405,380 L0,380 Z" fill="url(#glowFront)"/>
    <path d="M0,228 C60,110 200,20 420,0 L430,0 C210,35 75,140 0,258 Z" fill="var(--green)"/>
    <path d="M0,350 Q250,400 420,362 Q620,320 790,262 L790,285 Q620,340 420,378 Q250,410 0,365 Z" fill="url(#goldBand)"/>
    <path d="M0,362 Q250,410 420,372 Q620,330 790,280 L790,430 L0,430 Z" fill="var(--green)"/>
  </svg>

  <div class="brand"><span class="brand__mark"></span><span class="brand__name">BRIVEN WORKS</span></div>

  <h2 class="list-heading list-heading--achieve">Achieve Resolutions List</h2>
  <ul class="bullet-list bullet-list--achieve">
    <li>Find a experienced full service dental lab</li>
    <li>Lab that is FDA and KTRC certified.</li>
    <li>Competitive prices.</li>
    <li>Has consistent quality restorations and products.</li>
    <li>Briven Works</li>
  </ul>

  <h1 class="list-heading list-heading--resolutions">New Years Resolutions List</h1>
  <ul class="resolution-list">
    <li><svg viewBox="0 0 26 26"><path d="M2,14 L9,22 L24,3" fill="none" stroke="#111" stroke-width="4" stroke-linecap="round" stroke-linejoin="round"/></svg>Work less hours while maintaining current income</li>
    <li><svg viewBox="0 0 26 26"><path d="M2,14 L9,22 L24,3" fill="none" stroke="#111" stroke-width="4" stroke-linecap="round" stroke-linejoin="round"/></svg>Expand current dental lab</li>
    <li><svg viewBox="0 0 26 26"><path d="M2,14 L9,22 L24,3" fill="none" stroke="#111" stroke-width="4" stroke-linecap="round" stroke-linejoin="round"/></svg>Make more money with less headaches.</li>
    <li><svg viewBox="0 0 26 26"><path d="M2,14 L9,22 L24,3" fill="none" stroke="#111" stroke-width="4" stroke-linecap="round" stroke-linejoin="round"/></svg>Gain more freedom from long hours behind bench.</li>
  </ul>

  <div class="phone">
    <span class="phone__icon"><svg viewBox="0 0 24 24"><path d="M6.6 10.8c1.4 2.8 3.8 5.1 6.6 6.6l2.2-2.2c.3-.3.7-.4 1-.2 1.1.4 2.3.6 3.6.6.6 0 1 .4 1 1V20c0 .6-.4 1-1 1C10.6 21 3 13.4 3 4c0-.6.4-1 1-1h3.5c.6 0 1 .4 1 1 0 1.3.2 2.5.6 3.6.1.3 0 .7-.2 1z" fill="var(--green)"/></svg></span>
    855 314 9087
  </div>
  <p class="testimonial testimonial--front">Impressive work....better than<br>what we can do locally!...</p>
  <p class="trial-offer">*Special trial offer* 5 free PFM's!</p>
</section>

<section class="postcard postcard--back">
  <svg class="postcard__art" viewBox="0 0 790 430" preserveAspectRatio="none" aria-hidden="true">
    <defs>
      <radialGradient id="glowBack" cx="0.7" cy="0.45" r="0.8">
        <stop offset="0" stop-color="#fff3a0"/>
        <stop offset="0.6" stop-color="#fbe985"/>
        <stop offset="1" stop-color="#fff8cf"/>
      </radialGradient>
      <linearGradient id="goldBandBack" x1="0" x2="1">
        <stop offset="0" stop-color="#f4d23c"/>
        <stop offset="0.6" stop-color="#d9a400"/>
        <stop offset="1" stop-color="#7a5a10"/>
      </linearGradient>
    </defs>
    <path d="M0,150 C60,95 200,35 405,0 L405,390 L0,390 Z" fill="url(#glowBack)"/>
    <path d="M0,130 C60,80 200,30 420,0 L430,0 C210,40 75,100 0,160 Z" fill="var(--green)"/>
    <path d="M0,385 Q250,400 420,362 Q620,320 790,262 L790,285 Q620,340 420,378 Q250,412 0,398 Z" fill="url(#goldBandBack)"/>
    <path d="M0,394 Q250,412 420,372 Q620,330 790,280 L790,430 L0,430 Z" fill="var(--green)"/>
  </svg>

  <div class="brand"><span class="brand__mark"></span><span class="brand__name">BRIVEN WORKS</span></div>

  <ul class="bullet-list bullet-list--features">
    <li>ISO 9001, 13485 and FDA certified.</li>
    <li>Restorative Goods Quality Review Scheme (RGQRS) certified.</li>
    <li>5 year warranty on fixed and 2 years on removable.</li>
    <li>Local customer service in Phoenix Arizona assigned to your office and cases.</li>
    <li>Higher productivity- allows you to provide more units from your lab with the same number of technicians.</li>
  </ul>

  <div class="mailing-divider"></div>
  <div class="stamp-box"></div>
  <div class="address-line" style="top:194px"></div>
  <div class="address-line" style="top:226px"></div>
  <div class="address-line" style="top:257px"></div>
  <div class="address-line" style="top:289px"></div>

  <div class="phone">
    <span class="phone__icon"><svg viewBox="0 0 24 24"><path d="M6.6 10.8c1.4 2.8 3.8 5.1 6.6 6.6l2.2-2.2c.3-.3.7-.4 1-.2 1.1.4 2.3.6 3.6.6.6 0 1 .4 1 1V20c0 .6-.4 1-1 1C10.6 21 3 13.4 3 4c0-.6.4-1 1-1h3.5c.6 0 1 .4 1 1 0 1.3.2 2.5.6 3.6.1.3 0 .7-.2 1z" fill="var(--green)"/></svg></span>
    855 314 9087
  </div>
  <p class="testimonial testimonial--back">Thanks for your wonderful service,<br>our business is increasing by 20 per month...</p>
  <p class="trial-offer">*Special trial offer* 5 free PFM's!</p>
</section>

</body>
</html>
```